Design a Flyer for new years eve

Celebrate (ring in) new years at Vellora Restaurant
Call to make a reservation (415) 382 - 5904

Featuring Daniel Osmer with Acoustic Guitar (nights live entertainment)

Materials could be found
www.velloradining.com
www.facebook.com/velloradining
www.instagram.com/velloradining

Daniel's only picture we have is the one uploaded, feel free to search the web for more if you want.

We want a flyer that is elegant and reflects the ambiance of a classy Mediterranean restaurant.

```html
<!DOCTYPE html>
<html lang="en">
<head>
<meta charset="utf-8">
<title>New Year Party Flyer – Vellora Restaurant</title>
<link href="https://fonts.googleapis.com/css2?family=Oswald:wght@400;500&family=Saira+Condensed:wght@400;500&family=Saira+Semi+Condensed:wght@300;400;600&display=swap" rel="stylesheet">
<style>
  :root {
    --stage: #2a2f35;
    --flyer-dark: #0b0d12;
    --flyer-mid: #1a1e26;
    --line: rgba(235, 238, 245, 0.85);
    --text: #eef0f4;
    --text-soft: #c8ccd4;
    --gold-light: #f4f2c6;
    --gold: #d9cf6a;
    --gold-deep: #a99a32;
  }
  * { margin: 0; padding: 0; box-sizing: border-box; }
  html, body { width: 1200px; height: 963px; overflow: hidden; }
  body {
    background: var(--stage);
    position: relative;
    font-family: "Saira Semi Condensed", sans-serif;
    color: var(--text);
  }
  .flyer {
    position: absolute;
    left: 317px; top: 68px;
    width: 566px; height: 827px;
    overflow: hidden;
    background:
      radial-gradient(ellipse 60% 35% at 70% 30%, rgba(120,130,150,0.22), transparent 70%),
      linear-gradient(180deg, var(--flyer-mid) 0%, var(--flyer-dark) 55%, var(--flyer-dark) 100%);
  }
  .flyer__backdrop {
    position: absolute; left: 0; right: 0; bottom: 0; height: 360px;
    background:
      radial-gradient(ellipse 45% 40% at 40% 45%, rgba(150,140,125,0.32), transparent 75%),
      linear-gradient(180deg, transparent 0%, rgba(60,55,50,0.35) 50%, rgba(20,20,22,0.6) 100%);
  }
  .flyer__frame { position: absolute; inset: 0; }
  .flyer__text { position: absolute; left: 0; width: 100%; text-align: center; }
  .website { top: 8px; font-size: 13px; letter-spacing: 1.5px; color: var(--text-soft); }
  .headline-top {
    top: 118px; font-family: "Oswald", sans-serif; font-weight: 500;
    font-size: 40px; letter-spacing: 1px; color: var(--text-soft);
  }
  .headline-year {
    top: 150px; font-family: "Saira Condensed", sans-serif; font-weight: 500;
    font-size: 228px; line-height: 1; letter-spacing: 4px;
    background: linear-gradient(180deg, var(--gold-light) 0%, var(--gold) 45%, var(--gold-deep) 100%);
    -webkit-background-clip: text; background-clip: text; color: transparent;
  }
  .headline-bottom {
    top: 350px; font-family: "Oswald", sans-serif; font-weight: 500;
    font-size: 72px; line-height: 1; letter-spacing: 1px; color: var(--text);
  }
  .venue { top: 566px; font-size: 34px; font-weight: 400; letter-spacing: 1px; }
  .performer-label { top: 628px; font-size: 15px; font-weight: 600; letter-spacing: 3px; }
  .performer-name { top: 653px; font-size: 11px; letter-spacing: 0.5px; color: var(--text-soft); text-transform: uppercase; }
  .reserve-label { top: 692px; font-size: 18px; letter-spacing: 2px; }
  .reserve-phone { top: 716px; font-size: 18px; letter-spacing: 2px; }
  .divider {
    position: absolute; top: 748px; left: 203px; width: 160px;
    border-top: 1px dotted var(--text-soft);
  }
  .address { top: 759px; font-size: 11px; letter-spacing: 1px; color: var(--text-soft); }
  .social {
    position: absolute; top: 793px; display: flex; align-items: center; gap: 8px;
    font-size: 12px; letter-spacing: 1px; color: var(--text-soft);
  }
  .social--left { left: 112px; }
  .social--right { left: 322px; }
  .social__mark { width: 14px; height: 14px; border: 1px solid var(--text-soft); }
</style>
</head>
<body>
  <main class="flyer">
    <div class="flyer__backdrop" role="img" aria-label="Soft blurred photo of the guitarist performing, with warm bokeh lights"></div>

    <svg class="flyer__frame" width="566" height="827" viewBox="0 0 566 827" fill="none" stroke="var(--line)" stroke-width="1.2">
      <line x1="113" y1="0.6" x2="448" y2="0.6"/>
      <polyline points="113,0.6 283,45 448,0.6" stroke-opacity="0"/>
      <polygon points="283,55 487,171 487,397 283,491 73,397 73,171"/>
      <polyline points="140,0.6 283,58"/>
      <polyline points="426,0.6 283,58"/>
      <polyline points="77,827 77,571 283,475 489,571 489,827"/>
    </svg>

    <p class="flyer__text website">www.velloradining.com</p>
    <h1 class="flyer__text headline-top">NEW YEAR</h1>
    <p class="flyer__text headline-year">2018</p>
    <p class="flyer__text headline-bottom">PARTY</p>

    <h2 class="flyer__text venue">Vellora Restaurant</h2>
    <p class="flyer__text performer-label">SPECIAL PERFORMANCE BY</p>
    <p class="flyer__text performer-name">Daniel Osmer with acoustic guitar</p>
    <p class="flyer__text reserve-label">Call to make a reservation</p>
    <p class="flyer__text reserve-phone">(415) 382 - 5904</p>
    <div class="divider"></div>
    <p class="flyer__text address">18 Harbor Ln, Sausalito, CA - 94965</p>

    <p class="social social--left"><span class="social__mark"></span>/velloradining</p>
    <p class="social social--right"><span class="social__mark"></span>/velloradining</p>
  </main>
</body>
</html>
```